Design trifold flyer for patients

Hi buddy,I need a trifold brochure for an early event that month. I just need a design template in Adobe Illustrator, so that I can modify it later.Size: A4 divide into 3 pages, 10x21cm each. The total has 6 page with both sides.Content: (Page)1. Cover with logo, address, phone number, etc..2. Instruction: An image and a paragraph3 + 4. A content list, paragraph5. Note with patients6. Price listColor: blue and light blue, greenTarget audience: Patients

Target Market(s)

Patients in hospital

Industry/Entity Type

Medical

Font styles to use
Sans Serif

Colors
85cae6
33b8a4
0692cd

Requirements
Must have
• picture place holder
Nice to have
• icon

```html
<!DOCTYPE html>
<html lang="en">
<head>
<meta charset="utf-8">
<title>Riverside Care Hospital – Patient Trifold</title>
<link href="https://fonts.googleapis.com/css2?family=Open+Sans:wght@400;600;700&family=Raleway:wght@700;800&display=swap" rel="stylesheet">
<style>
  :root {
    --canvas: #e8e8e8;
    --paper: #ffffff;
    --paper-grey: #f3f4f5;
    --blue: #0692cd;
    --blue-mid: #3a9bd8;
    --sky: #85cae6;
    --mist-top: #e6eef4;
    --mist-bottom: #c9d7e1;
    --slate-top: #b8c9d6;
    --slate-bottom: #9fb3c3;
    --green: #6ab54a;
    --ink: #2b2f33;
    --ink-soft: #4a5560;
    --rule: #d7dadd;
    --brand: #3f63b3;
  }
  * { box-sizing: border-box; margin: 0; padding: 0; }
  html, body { width: 1200px; height: 906px; overflow: hidden; }
  body { background: var(--canvas); font-family: "Open Sans", Arial, sans-serif; }

  .trifold {
    position: absolute; left: 30px; top: 50px;
    width: 1140px; height: 806px;
    display: flex;
    box-shadow: 0 10px 30px rgba(0,0,0,.18);
  }
  .panel { position: relative; width: 380px; height: 806px; overflow: hidden; }

  /* Panel: instruction */
  .panel--intro { background: linear-gradient(180deg, var(--slate-top), var(--slate-bottom)); }
  .intro__photo {
    position: absolute; left: 0; top: 0; width: 380px; height: 420px;
    background: linear-gradient(160deg, #a9c3d8 0%, #cfdde6 40%, #8b7866 75%, #5d5248 100%);
  }
  .intro__caption {
    position: absolute; left: 0; top: 330px; width: 380px; height: 90px;
    background: rgba(40,38,36,.72);
    color: #fff; font-family: "Raleway", Arial, sans-serif; font-weight: 700;
    font-size: 22px; line-height: 1.2; padding: 18px 30px;
  }
  .intro__text {
    position: absolute; left: 30px; top: 450px; width: 320px;
    font-size: 11.5px; line-height: 1.6; color: var(--ink-soft);
  }

  /* Panel: price list */
  .panel--prices { background: var(--paper-grey); }
  .prices__table { position: absolute; left: 30px; top: 40px; }

  /* Panel: cover */
  .panel--cover { background: linear-gradient(180deg, var(--mist-top), var(--mist-bottom)); }
  .cover__brand {
    position: absolute; left: 30px; top: 34px;
    display: flex; align-items: center; gap: 10px;
    color: var(--brand); font-weight: 700; font-size: 17px; letter-spacing: .04em;
  }
  .cover__brand-mark { width: 16px; height: 16px; background: var(--brand); }
  .cover__photo {
    position: absolute; left: 0; top: 80px; width: 380px; height: 350px;
    background: linear-gradient(150deg, #f4f6f8 0%, #dfe5ea 45%, #c9b3ae 75%, #9e8f8c 100%);
  }
  .cover__badge { position: absolute; left: 30px; top: 398px; }
  .cover__title {
    position: absolute; left: 120px; top: 470px;
    font-family: "Raleway", Arial, sans-serif; font-weight: 800;
    font-size: 40px; line-height: 1.02; color: var(--ink);
  }
  .cover__org {
    position: absolute; left: 30px; top: 640px; width: 110px;
    font-size: 12px; font-weight: 700; line-height: 1.3; color: var(--ink);
  }
  .cover__text {
    position: absolute; left: 150px; top: 640px; width: 200px;
    font-size: 11px; line-height: 1.55; color: var(--ink-soft);
  }
</style>
</head>
<body>
<main class="trifold">

  <section class="panel panel--intro">
    <div class="intro__photo" role="img" aria-label="Photo of an expectant mother seated on a wooden terrace swing under a pale sky"></div>
    <h2 class="intro__caption">Harumque praeribus<br>moluptatem</h2>
    <p class="intro__text">Mini, offic tet quo nectate nonsequam alicia delitatures pro conseque laccustios nditior sanit, tem aliquamus volorerum te rerumquo commimo ghihit eatur rerum et quas ea vollita quiaectatis essam utatiost ducit re, seque volorem fuga. Conectio ma iuscae nobis auciorum, tet por re con nus aut inulpa nonsequo tet utat. Excerias pelitatioreo velit qui dae volut ut odis volorum eserum renectus as lique nat aperit ame ed aut la dolora quo tote veni poris dolorem quas re aute et quat odiscae sequam. Sedit la debit is culpari assitatempe alibus, tempel iquaspe duciente volupta tiundem faccabo. Nihil molestio officia qui ut omnis sitae plaborer.</p>
  </section>

  <section class="panel panel--prices">
    <svg class="prices__table" width="320" height="730" viewBox="0 0 320 730" aria-label="Price list table">
      <defs>
        <pattern id="row-lines" width="320" height="16" patternUnits="userSpaceOnUse">
          <rect width="320" height="16" fill="#fff"/>
          <line x1="0" y1="15.5" x2="320" y2="15.5" stroke="#d7dadd" stroke-width="1"/>
        </pattern>
      </defs>
      <rect x="0" y="0" width="320" height="730" fill="url(#row-lines)" stroke="#d7dadd"/>
      <line x1="250" y1="0" x2="250" y2="730" stroke="#d7dadd"/>
      <line x1="288" y1="0" x2="288" y2="730" stroke="#d7dadd"/>
      <g fill="#0692cd">
        <rect x="0" y="0" width="320" height="14"/>
        <rect x="0" y="96" width="320" height="14"/>
        <rect x="0" y="160" width="320" height="14"/>
        <rect x="0" y="256" width="320" height="14"/>
        <rect x="0" y="304" width="320" height="14"/>
        <rect x="0" y="400" width="320" height="14"/>
        <rect x="0" y="544" width="320" height="14"/>
        <rect x="0" y="608" width="320" height="14"/>
        <rect x="0" y="656" width="320" height="14"/>
      </g>
      <g fill="#3a9bd8" opacity=".55">
        <rect x="250" y="0" width="70" height="14"/>
        <rect x="250" y="400" width="70" height="14"/>
      </g>
    </svg>
  </section>

  <section class="panel panel--cover">
    <div class="cover__brand"><span class="cover__brand-mark"></span>RIVERSIDE CARE HOSPITAL</div>
    <div class="cover__photo" role="img" aria-label="Photo of a smiling young couple at home holding a paper heart"></div>
    <svg class="cover__badge" width="48" height="48" viewBox="0 0 48 48" aria-label="Care icon">
      <circle cx="24" cy="24" r="24" fill="#6ab54a"/>
      <path d="M20 13h8v7h7v8h-7v7h-8v-7h-7v-8h7z" fill="#fff"/>
    </svg>
    <h1 class="cover__title">Soluptae<br>essin re,<br>soluptat</h1>
    <p class="cover__org">Riverside Care Hospital</p>
    <p class="cover__text">Excerovid utem que velit accaerovit ipsam lab ipsus, serovid eum as am id unto il mi, sin reiuscium dolupta sperep tatus, coribus. Es et fugit es et venis essandi gnienda orecat modi to volorem dolupiae dolores aute etur? Es nati optiatur?</p>
  </section>

</main>
</body>
</html>
```